Lab & Medical Equipment Repair Company Business Card Design

Looking for business card design for a lab & medical equipment repair company. Must be double-sided and must list our primary pieces we repair. Optionally, can include a QR code which should direct to our website.

Clients are usually doctors, so the card must be designed with a professional tone; however, we are looking for creativity in presentation. Open as to what should be on the front and back on card.

** Looking for a CLEAN design with creativity. Please use "Nice to have Priorities" items with discretion.

Core marketing logic:

When lab or medical equipment needs repair, most doctors call the manufacturers and schedule a technician to repair. Usually this takes one or two weeks, and, often, their work spoils. Alternatively, the doctors could hold equipment insurance which gives them a less expensive cost, but the response time is still similarly long.

Our company provides both competitive rates and one of the fastest response times in the industry. Technicians are dispatched directly to the site of the equipment, usually within 24 hours. Equipment under contract receives the same fast response time and includes complimentary annual maintenance. We service some of the most prestigious facilities in the Pittsburgh area and cover all of Western Pennsylvania, Ohio, and West Virginia.

Target Market(s)

Laboratory owners (doctors)

Industry/Entity Type

Marketing

Requirements
Must have
• Company Logo
Employee Name: Ray Dunwoody
Employee Title: CEO
Company Phone: 724-555-0187
Company Fax: 866-555-0143
Company Address: PO Box 518 Harmony Glen, PA 16099
Company Website: www.brightfixlabtech.example
Equipment We Service: Freezers, Cryostorage, Incubators, Centrifuges, Refrigerators, Environmental Chambers, Autoclaves, and more.

Nice to have
• Company Facebook: facebook.com/bfltllc
Company Twitter: @BFLTLLC
QR Code (link to website): www.brightfixlabtech.example

```html
<!DOCTYPE html>
<html lang="en">
<head>
<meta charset="utf-8">
<title>BFLT Business Card</title>
<link rel="stylesheet" href="https://fonts.googleapis.com/css2?family=Didact+Gothic&display=swap">
<style>
  :root {
    --stage: #2b2d2c;
    --card: #ffffff;
    --band: #d1d2d4;
    --green: #2db34a;
    --ink: #1b1b1b;
    --text: #2a2a2a;
    --shadow: rgba(0, 0, 0, 0.55);
  }
  * { margin: 0; padding: 0; box-sizing: border-box; }
  html, body {
    width: 1200px; height: 1200px; overflow: hidden;
    background: var(--stage);
    font-family: "Didact Gothic", sans-serif;
  }
  .canvas { position: relative; width: 1200px; height: 1200px; }
  .card {
    position: absolute; left: 142px; width: 901px; height: 501px;
    background: var(--card);
    box-shadow: 6px 8px 10px var(--shadow);
  }
  .card--front { top: 62px; }
  .card--back { top: 630px; }

  .name-band {
    position: absolute; left: 211px; top: 0; width: 690px; height: 216px;
    background: var(--band);
  }
  .person-name {
    position: absolute; left: 39px; top: 70px;
    font-size: 47px; font-weight: 400; color: var(--green); line-height: 1;
    letter-spacing: -0.5px;
  }
  .person-title {
    position: absolute; left: 39px; top: 134px;
    font-size: 27px; color: var(--text); line-height: 1;
  }
  .side-mark {
    position: absolute; left: 98px; top: 252px;
    transform: translate(-50%, -50%) rotate(-90deg);
    display: flex; align-items: center; gap: 18px;
    white-space: nowrap;
  }
  .brand-name {
    font-size: 96px; color: var(--ink); line-height: 1; letter-spacing: 4px;
  }
  .side-mark .brand-name { font-size: 92px; }
  .brand-dot {
    width: 26px; height: 26px; border-radius: 50%; background: var(--green);
  }
  .contact-list {
    position: absolute; left: 250px; top: 256px;
    list-style: none; font-size: 28px; color: var(--text);
    line-height: 38px; letter-spacing: -0.3px;
  }
  .contact-label--fax { display: inline-block; width: 80px; }

  .back-mark {
    position: absolute; left: 0; top: 98px; width: 100%;
    display: flex; justify-content: center; align-items: center; gap: 22px;
  }
  .back-mark .brand-name { font-size: 112px; }
  .back-mark .brand-dot { width: 30px; height: 30px; }
  .service-block {
    position: absolute; left: 0; top: 300px; width: 100%;
    text-align: center; font-size: 28px; line-height: 38px; color: var(--text);
  }
  .service-heading { color: var(--green); }
</style>
</head>
<body>
<main class="canvas">
  <section class="card card--front" aria-label="Card front">
    <div class="side-mark">
      <span class="brand-name">BFLT</span>
      <span class="brand-dot"></span>
    </div>
    <div class="name-band">
      <h1 class="person-name">Ray Dunwoody</h1>
      <p class="person-title">CEO</p>
    </div>
    <ul class="contact-list">
      <li>Phone: 724-555-0187</li>
      <li><span class="contact-label--fax">Fax:</span>866-555-0143</li>
      <li>Address: PO Box 518 Harmony Glen, PA 16099</li>
      <li>Website: www.brightfixlabtech.example</li>
    </ul>
  </section>

  <section class="card card--back" aria-label="Card back">
    <div class="back-mark">
      <span class="brand-name">BFLT</span>
      <span class="brand-dot"></span>
    </div>
    <div class="service-block">
      <p class="service-heading">Equipment we service:</p>
      <p>Freezers, Cryostorage, Incubators, Centrifuges, Refrigerators,</p>
      <p>Environmental Chambers, Autoclaves, and more!</p>
    </div>
  </section>
</main>
</body>
</html>
```